furnace plenum sticker

This sticker is left at every job above the furnace or on the duct work connected to the furnace.
It needs to be bold so that when homeowner is at the furnace during a break down they see it. Phone number and what we do needs to be prominate. It is our calling card for service.
Sticker needs to look corporate and professional.

New logo (attached) must be incorporated into sticker.

Current sticker attached
Size
8.5 inches x 5.5 inches

Target Market(s)

residential home owners

Industry/Entity Type

Work

Colors
ec1f27

Requirements
Must have
• Our new current logo attached

```html
<!DOCTYPE html>
<html lang="en">
<head>
<meta charset="utf-8">
<title>Maplegrove Furnace Plenum Sticker</title>
<link href="https://fonts.googleapis.com/css2?family=Open+Sans:wght@600;700;800&display=swap" rel="stylesheet">
<style>
  :root {
    --brand-red: #ec1f27;
    --ink: #111111;
    --paper: #ffffff;
    --backdrop: #e9e9e9;
  }
  * { margin: 0; padding: 0; box-sizing: border-box; }
  html, body { width: 1200px; height: 1200px; overflow: hidden; }
  body {
    background: var(--backdrop);
    font-family: "Open Sans", Arial, sans-serif;
    position: relative;
  }
  .sticker {
    position: absolute;
    left: 59px; top: 275px;
    width: 1082px; height: 649px;
    background: var(--paper);
    overflow: hidden;
  }
  .band { position: absolute; left: 0; width: 100%; background: var(--brand-red); }
  .band--top-thick   { top: 0;   height: 34px; }
  .band--top-thin    { top: 44px; height: 12px; }
  .band--mid-thin    { top: 326px; height: 16px; }
  .band--contact     { top: 352px; height: 186px; }
  .band--low-thin    { top: 547px; height: 11px; }
  .band--base-thin   { top: 612px; height: 10px; }
  .band--base-thick  { top: 630px; height: 19px; }

  .brand {
    position: absolute; left: 0; top: 56px; width: 100%; height: 270px;
    display: flex; flex-direction: column; align-items: center; justify-content: center;
    color: var(--brand-red); font-weight: 800; text-align: center;
  }
  .brand__name { font-size: 112px; line-height: 1; letter-spacing: 2px; }
  .brand__trade { font-size: 38px; line-height: 1.2; margin-top: 8px; letter-spacing: 0.5px; }

  .contact {
    position: absolute; top: 352px; height: 186px; width: 500px;
    text-align: center; color: var(--paper);
  }
  .contact--left { left: 38px; }
  .contact--right { left: 570px; }
  .contact__phone {
    display: block; margin-top: 42px;
    font-size: 54px; font-weight: 600; letter-spacing: 5px; line-height: 1.1;
    -webkit-text-stroke: 1.5px var(--ink);
    text-shadow: 3px 4px 8px rgba(0,0,0,0.75);
  }
  .contact__area {
    display: block; margin-top: 14px;
    font-size: 29px; font-weight: 800; letter-spacing: 1px; line-height: 1;
  }

  .services {
    position: absolute; left: 28px; right: 22px; top: 558px; height: 54px;
    display: flex; justify-content: space-between; align-items: center;
    font-size: 23px; font-weight: 800; color: var(--ink); letter-spacing: 0.2px;
  }
</style>
</head>
<body>
  <main class="sticker">
    <div class="band band--top-thick"></div>
    <div class="band band--top-thin"></div>

    <header class="brand">
      <span class="brand__name">MAPLEGROVE</span>
      <span class="brand__trade">HEATING AND AIR CONDITIONING</span>
    </header>

    <div class="band band--mid-thin"></div>
    <div class="band band--contact"></div>

    <section class="contact contact--left">
      <span class="contact__phone">905-555-0137</span>
      <span class="contact__area">BURLINGTON/HAMILTON</span>
    </section>
    <section class="contact contact--right">
      <span class="contact__phone">905-555-0182</span>
      <span class="contact__area">OAKVILLE/MILTON</span>
    </section>

    <div class="band band--low-thin"></div>

    <footer class="services">
      <span>24 HOURS SERVICE.</span>
      <span>WE SERVICE ALL MAKES &amp; MODELS.</span>
      <span>REPAIRS &amp; INSTALLATIONS</span>
    </footer>

    <div class="band band--base-thin"></div>
    <div class="band band--base-thick"></div>
  </main>
</body>
</html>
```